Startup Drone Platform Company business card

We are needing a business card design for our employees. We are a startup drone platform. We are looking for a business card that has our logo on one side, with the employee/company details on the opposite side. We are looking for something that is very eye catching, modern, and bold.

Target Market(s)

This will target both drone pilots and drone businesses, along with all the industries that could utilize drone services (aerial video, aerial photos, inspections, 3d mapping, etc).

Industry/Entity Type

Business

```html
<!DOCTYPE html>
<html lang="en">
<head>
<meta charset="utf-8">
<title>Skyfleet Business Card</title>
<link rel="stylesheet" href="https://fonts.googleapis.com/css2?family=Montserrat:wght@400;500;600&display=swap">
<style>
  :root {
    --page: #e9e9e7;
    --ink: #1c1c1c;
    --black-card: #0d0d0d;
    --teal: #3fc4cf;
    --teal-light: #7ad8df;
    --teal-deep: #2fb2bf;
    --white: #ffffff;
    --paper: #f4f4f4;
    --ring: #151515;
  }
  * { box-sizing: border-box; margin: 0; padding: 0; }
  html, body {
    width: 1200px; height: 843px; overflow: hidden;
    background: var(--page);
    font-family: "Montserrat", sans-serif;
  }
  .canvas { position: relative; width: 1200px; height: 843px; }

  .card {
    position: absolute;
    width: 620px; height: 354px;
    overflow: hidden;
    box-shadow: 0 10px 24px rgba(0,0,0,0.22);
  }

  /* Logo side */
  .card--logo {
    left: 90px; top: 60px;
    background: linear-gradient(160deg, #1e1e1e 0%, var(--black-card) 55%);
    color: var(--white);
  }
  .card--logo .brand {
    position: absolute; left: 0; right: 0; top: 150px;
    display: flex; justify-content: center; align-items: center; gap: 22px;
  }
  .card--logo .brand-name {
    font-weight: 400; font-size: 30px; letter-spacing: 14px;
    margin-right: -14px;
  }
  .brand-dot {
    width: 16px; height: 16px; border-radius: 50%;
    background: var(--white);
  }
  .card--logo .web {
    position: absolute; left: 0; right: 0; bottom: 48px;
    text-align: center; font-size: 13px; letter-spacing: 7px;
  }

  /* Details side */
  .card--details {
    left: 490px; top: 440px;
    background: linear-gradient(120deg, var(--teal-light) 0%, var(--teal) 35%, var(--teal-deep) 100%);
    color: var(--white);
  }
  .card-shape { position: absolute; inset: 0; }

  .person { position: absolute; left: 34px; top: 30px; }
  .person-name { font-weight: 600; font-size: 19px; }
  .person-role { font-size: 13px; margin-top: 2px; }

  .address { position: absolute; left: 34px; top: 104px; font-size: 13px; line-height: 1.4; }

  .contacts { position: absolute; left: 34px; top: 160px; list-style: none; font-size: 13px; }
  .contacts li { display: flex; align-items: center; gap: 12px; height: 23px; }
  .contacts svg { width: 14px; height: 14px; fill: var(--white); flex: none; }

  .card--details .brand {
    position: absolute; left: 330px; width: 290px; top: 150px;
    display: flex; flex-direction: column; align-items: center; gap: 14px;
    color: var(--ink);
  }
  .card--details .brand-dot {
    width: 58px; height: 58px; background: var(--teal);
  }
  .card--details .brand-name {
    font-weight: 500; font-size: 28px; letter-spacing: 9px; margin-right: -9px;
  }
</style>
</head>
<body>
<main class="canvas">

  <section class="card card--logo" aria-label="Card front">
    <div class="brand">
      <span class="brand-name">SKYFLEET</span>
      <span class="brand-dot"></span>
    </div>
    <p class="web">www.skyfleet.co</p>
  </section>

  <section class="card card--details" aria-label="Card back">
    <svg class="card-shape" viewBox="0 0 620 354" aria-hidden="true">
      <defs>
        <linearGradient id="paperFade" x1="0" y1="0" x2="1" y2="1">
          <stop offset="0" stop-color="#ffffff"/>
          <stop offset="1" stop-color="#e4e4e4"/>
        </linearGradient>
      </defs>
      <circle cx="560" cy="215" r="278" fill="var(--ring)"/>
      <circle cx="566" cy="218" r="272" fill="url(#paperFade)"/>
    </svg>

    <div class="person">
      <p class="person-name">Marcus Hale</p>
      <p class="person-role">President</p>
    </div>

    <p class="address">2170 Larkspur Avenue<br>Glen Haven, NY 11020</p>

    <ul class="contacts">
      <li>
        <svg viewBox="0 0 16 16"><path d="M2 5c0-2 2-3 6-3s6 1 6 3v1h-3V5H5v1H2zM4 7h8l2 7H2z"/></svg>
        555 0142 7781
      </li>
      <li>
        <svg viewBox="0 0 16 16"><rect x="4" y="1" width="8" height="14" rx="1.5"/></svg>
        555 0193 4426
      </li>
      <li>
        <svg viewBox="0 0 16 16"><rect x="4" y="1" width="8" height="5"/><rect x="1" y="6" width="14" height="7" rx="1"/></svg>
        555 0167 2093
      </li>
      <li>
        <svg viewBox="0 0 16 16"><path d="M1 3h14v10H1zM2 4l6 5 6-5v-.5H2z"/></svg>
        marcus@skyfleet.co
      </li>
      <li>
        <svg viewBox="0 0 16 16"><circle cx="8" cy="8" r="7"/></svg>
        www.skyfleet.co
      </li>
    </ul>

    <div class="brand">
      <span class="brand-dot"></span>
      <span class="brand-name">SKYFLEET</span>
    </div>
  </section>

</main>
</body>
</html>
```